Letterhead and Stationary for Construction Company

Brisk Current needs modern Letterhead, Envelopes and Notepad designs.

Industry/Entity Type

Construction

Colors
f78f20
34a7d8
ffffff

Requirements
Must have
• Modern looking design.

```html
<!DOCTYPE html>
<html lang="en">
<head>
<meta charset="utf-8">
<title>Brisk Current – Stationery</title>
<link href="https://fonts.googleapis.com/css2?family=Lato:wght@400;700;900&display=swap" rel="stylesheet">
<style>
  :root {
    --orange: #e8772a;
    --blue: #2a73b8;
    --paper: #ffffff;
    --backdrop: #dcdcdc;
    --ink: #4a4a4a;
    --ink-dark: #222222;
    --ghost: #f4f4f4;
    --window: #ededed;
    --rule: #555555;
  }
  * { box-sizing: border-box; margin: 0; padding: 0; }
  html, body { width: 1200px; height: 860px; overflow: hidden; }
  body {
    background: var(--backdrop);
    font-family: "Lato", Arial, sans-serif;
    color: var(--ink);
    position: relative;
  }

  .sheet {
    position: absolute;
    background: var(--paper);
    box-shadow: 0 6px 18px rgba(0,0,0,0.12);
    overflow: hidden;
  }

  .brand {
    display: flex;
    align-items: center;
    gap: 10px;
    position: relative;
    z-index: 2;
  }
  .brand-dot {
    width: 30px; height: 30px;
    border-radius: 50%;
    background: var(--orange);
    flex: none;
  }
  .brand-name {
    font-weight: 900;
    font-size: 26px;
    color: var(--blue);
    letter-spacing: -0.3px;
  }

  .ghost-circle {
    position: absolute;
    border-radius: 50%;
    border: 22px solid var(--ghost);
    z-index: 0;
  }

  .stripe {
    position: absolute;
    left: 0; right: 0; bottom: 0;
    height: 12px;
    display: flex;
    z-index: 2;
  }
  .stripe-orange { background: var(--orange); }
  .stripe-blue { background: var(--blue); flex: 1; }

  /* Letterhead */
  .letterhead {
    left: 60px; top: 90px;
    width: 470px; height: 680px;
    border-top: 3px solid var(--blue);
  }
  .letterhead .brand { position: absolute; left: 44px; top: 110px; }
  .contact-block {
    position: absolute;
    right: 40px; top: 40px;
    padding-left: 10px;
    border-left: 1px solid var(--rule);
    font-size: 8.5px;
    font-style: normal;
    line-height: 1.45;
    color: var(--ink-dark);
    z-index: 2;
  }
  .contact-line { display: flex; align-items: center; gap: 4px; }
  .contact-line svg { width: 8px; height: 8px; flex: none; }

  .letter-content {
    position: absolute;
    left: 44px; top: 190px;
    width: 382px;
    z-index: 2;
  }
  .letter-body {
    font-size: 9px;
    line-height: 1.5;
  }
  .letter-body p { margin-bottom: 11px; }
  .signature {
    margin-top: 10px;
    width: 130px; height: 36px;
    background: linear-gradient(90deg, #ececec, #f7f7f7);
  }
  .letterhead .ghost-circle { width: 230px; height: 230px; right: 36px; bottom: 40px; }
  .letterhead .stripe-orange { width: 50%; }

  /* Envelope back */
  .envelope-back {
    left: 590px; top: 110px;
    width: 560px; height: 280px;
  }
  .flap { position: absolute; left: 0; top: 0; width: 560px; height: 110px; }
  .flap-mark {
    position: absolute;
    top: 40px; left: 0; right: 0;
    text-align: center;
    font-weight: 900;
    font-size: 14px;
    color: var(--paper);
  }
  .return-address {
    position: absolute;
    left: 0; right: 0; bottom: 50px;
    text-align: center;
    font-size: 9px;
    color: var(--ink-dark);
  }

  /* Envelope front */
  .envelope-front {
    left: 590px; top: 460px;
    width: 560px; height: 280px;
  }
  .envelope-front .brand { position: absolute; left: 40px; top: 70px; }
  .address-window {
    position: absolute;
    left: 40px; top: 140px;
    width: 230px; height: 80px;
    background: var(--window);
    border: 1px solid #e0e0e0;
    border-radius: 4px;
    z-index: 2;
  }
  .envelope-front .ghost-circle { width: 180px; height: 180px; right: 30px; top: 20px; }
  .envelope-front .stripe-orange { width: 60%; }
</style>
</head>
<body>

  <section class="sheet letterhead" aria-label="Letterhead">
    <div class="ghost-circle" aria-hidden="true"></div>

    <div class="brand">
      <span class="brand-dot"></span>
      <span class="brand-name">Brisk Current</span>
    </div>

    <address class="contact-block">
      <div>Northfield Works, LLC</div>
      <div>218 Mill Lane</div>
      <div>Fairview, NJ 07022</div>
      <div class="contact-line">
        <svg viewBox="0 0 10 10"><path d="M2 1 L4 1 L5 3 L4 4 Q5 6 6 6 L7 5 L9 6 L9 8 Q8 9 7 9 Q1 8 1 2 Q1 1 2 1Z" fill="var(--blue)"/></svg>
        (555)310-4821
      </div>
      <div class="contact-line">
        <svg viewBox="0 0 10 10"><rect x="1" y="3" width="8" height="5" fill="var(--blue)"/><rect x="3" y="1" width="4" height="2" fill="var(--blue)"/></svg>
        (555)310-4800
      </div>
      <div class="contact-line">
        <svg viewBox="0 0 10 10"><rect x="1" y="2" width="8" height="6" fill="var(--blue)"/><path d="M1 2 L5 5.5 L9 2" stroke="#fff" fill="none"/></svg>
        office@briskcurrent.build
      </div>
      <div class="contact-line">
        <svg viewBox="0 0 10 10"><circle cx="5" cy="5" r="4" fill="var(--blue)"/></svg>
        www.briskcurrent.build
      </div>
    </address>

    <div class="letter-content">
      <div class="letter-body">
        <p>Lorem ipsum dolor sit amet, consectetur adipiscing elit. Praesent non est diam. Vivamus risus sem, gravida sit amet nibh ut, ornare lobortis ante. Aliquam sollicitudin, mauris tincidunt semper venenatis, orci est pretium augue, ut vestibulum felis velit bibendum urna. Integer sollicitudin aliquet ligula, non ultricies nisl efficitur nec. Aliquam felis lorem, facilisis ac condimentum quis, consectetur volutpat lacus. Proin fermentum sem quis elit efficitur, eu tempus magna maximus.</p>
        <p>Aenean a mi tortor. Morbi pretium mi sed cursus vehicula. Lorem ipsum dolor sit amet, consectetur adipiscing elit. In finibus eros ac maximus finibus. Nunc pretium pellentesque tellus. Nullam accumsan nisl non diam commodo sagittis. Nunc et ante sit amet urna auctor convallis. Maecenas sed fringilla metus, sit amet vulputate felis. Morbi eget tempor nisl. Aliquam erat volutpat. Aenean laoreet interdum tempus.</p>
        <p>Maecenas dignissim placerat mauris, vitae sollicitudin ex. Integer bibendum maximus mauris, ac tempor urna viverra id. Integer tincidunt lobortis nisl at posuere. Sed faucibus vulputate finibus. Maecenas convallis, sem quis pellentesque cursus, urna quam aliquam augue, quis porttitor eros est nec lectus. Sed mattis at tellus ut blandit. Aenean nunc magna, viverra sed mauris vel, porta finibus lacus. Nullam bibendum turpis rutrum porta placerat.</p>
      </div>
      <div class="signature" role="img" aria-label="Handwritten signature of Owen Hale"></div>
    </div>

    <div class="stripe" aria-hidden="true">
      <span class="stripe-orange"></span><span class="stripe-blue"></span>
    </div>
  </section>

  <section class="sheet envelope-back" aria-label="Envelope back">
    <svg class="flap" viewBox="0 0 560 110" aria-hidden="true">
      <path d="M0 0 H560 V40 Q560 52 548 56 L70 108 Q60 110 54 104 L0 52 Z" fill="var(--blue)"/>
    </svg>
    <div class="flap-mark">Brisk Current</div>
    <div class="return-address">1290 Alder Court • Suite 12 • Riverton • CA 95010</div>
  </section>

  <section class="sheet envelope-front" aria-label="Envelope front">
    <div class="ghost-circle" aria-hidden="true"></div>
    <div class="brand">
      <span class="brand-dot"></span>
      <span class="brand-name">Brisk Current</span>
    </div>
    <div class="address-window" aria-hidden="true"></div>
    <div class="stripe" aria-hidden="true">
      <span class="stripe-orange"></span><span class="stripe-blue"></span>
    </div>
  </section>

</body>
</html>
```